Detail Shop Business card design

i need a business card design for my new detailing company called 'Brenner's Detail Shop'. i want an all black and white design . simple, direct and to the point. i want the designer to choose a fitting font to match the logothe front should have logo, address, phone and email and the back side should have a slogan and text indicating that we offer services on anything including cars, trucks, motorcycles and RVs. slogan will read "we take pride in your ride"
maybe also very small on the back side the IG icon with Brenners_Detail_Shop

phone 482.615.7734
address 7384 E Harlow Ave
Marlow ID 99342
email: BrennersDetail@quorvail.com

Target Market(s)

all ages , auto enthusiasts

Industry/Entity Type

Automotive

Contact Information for Business Card

the front should have logo, address, phone and email and the back side should have a slogan and text indicating that we offer services on anything including cars, trucks, motorcycles and RVs. slogan will read "we take pride in your ride"

phone 482.615.7734
address 7384 E Harlow Ave
Marlow ID 99342

Colors
000000
ffffff

Requirements
Must have
• bold font and very simple design with good spacing
Nice to have
• anything creative from the designer indicating we service any types of vehicles
Should not have
• any colors ,

```html
<!DOCTYPE html>
<html lang="en">
<head>
<meta charset="utf-8">
<title>Brenner's Detail Shop – Business Cards</title>
<link rel="stylesheet" href="https://fonts.googleapis.com/css2?family=Source+Sans+3:wght@400;600;700&display=swap">
<style>
  :root {
    --backdrop: #3a332f;
    --card: #111111;
    --card-edge: #1c1c1c;
    --ink: #ffffff;
    --ink-soft: #d9d9d9;
    --ink-muted: #8a8a8a;
  }
  * { box-sizing: border-box; margin: 0; padding: 0; }
  html, body {
    width: 1200px;
    height: 864px;
    overflow: hidden;
    background: var(--backdrop);
    font-family: "Source Sans 3", "Myriad Pro", Arial, sans-serif;
    color: var(--ink);
  }
  .canvas {
    position: relative;
    width: 1200px;
    height: 864px;
    display: flex;
    align-items: center;
    justify-content: center;
    gap: 50px;
  }
  .card {
    width: 525px;
    height: 300px;
    background: var(--card);
    border: 1px solid var(--card-edge);
    box-shadow: 0 14px 30px rgba(0,0,0,0.45);
    position: relative;
  }
  /* Slogan side */
  .card--slogan {
    display: flex;
    flex-direction: column;
    align-items: center;
    justify-content: center;
    text-align: center;
    padding: 0 40px;
  }
  .brand-mark {
    display: flex;
    align-items: center;
    gap: 12px;
    margin-bottom: 34px;
  }
  .brand-mark__dot {
    width: 26px;
    height: 26px;
    border-radius: 50%;
    background: var(--ink-muted);
  }
  .brand-mark__name {
    font-size: 26px;
    font-weight: 700;
    color: var(--ink-muted);
    letter-spacing: 0.5px;
  }
  .slogan {
    font-size: 17px;
    font-weight: 700;
    text-transform: uppercase;
    letter-spacing: 0.4px;
    color: var(--ink-soft);
    padding-bottom: 6px;
    border-bottom: 1px solid var(--ink-muted);
    width: 290px;
  }
  .services {
    margin-top: 8px;
    font-size: 12.5px;
    font-weight: 600;
    color: var(--ink-muted);
  }
  /* Contact side */
  .card--contact {
    display: flex;
    align-items: center;
    justify-content: center;
  }
  .contact {
    text-align: left;
    font-size: 15px;
    line-height: 1.28;
    color: var(--ink-soft);
    margin-left: 40px;
  }
  .contact__name {
    font-size: 17px;
    font-weight: 700;
    color: var(--ink);
    letter-spacing: 0.3px;
  }
  .contact__title {
    font-size: 13px;
    letter-spacing: 0.6px;
    margin-bottom: 4px;
  }
</style>
</head>
<body>
  <main class="canvas">
    <section class="card card--slogan">
      <div class="brand-mark">
        <span class="brand-mark__dot"></span>
        <span class="brand-mark__name">Brenner's Detail Shop</span>
      </div>
      <p class="slogan">We take pride in your ride</p>
      <p class="services">we offer services on anything including cars, trucks, motorcycles &amp; RVs</p>
    </section>

    <section class="card card--contact">
      <div class="contact">
        <p class="contact__name">MARCUS VELL</p>
        <p class="contact__title">PRESIDENT</p>
        <p>7384 E Harlow Ave</p>
        <p>Marlow ID 99342</p>
        <p>(P) 482.615.7734</p>
        <p>(M) 647 205 3918</p>
        <p>BrennersDetail@quorvail.com</p>
        <p>www.brennersdetailshop.net</p>
      </div>
    </section>
  </main>
</body>
</html>
```